Redesign Colorful Business Card

Please redesign the card attached. It is too busy. Please don't eliminate any of the words. The repetivite word "free" can be used less often.

Target Market(s)

College Students.

Contact Information for Business Card

The details listed in the attached image

Font styles to use
Sans Serif

Requirements
Must have
• A clear and simple presentation and must be attractive.

```html
<!DOCTYPE html>
<html lang="en">
<head>
<meta charset="utf-8">
<title>Quillora.net Card</title>
<link href="https://fonts.googleapis.com/css2?family=Montserrat:wght@600;700;800&family=Open+Sans:wght@700&display=swap" rel="stylesheet">
<style>
  :root {
    --page-bg: #ffffff;
    --card-red: #ec5044;
    --accent-yellow: #fbe158;
    --text-white: #ffffff;
  }
  html, body {
    margin: 0;
    padding: 0;
    width: 1200px;
    height: 1000px;
    overflow: hidden;
    background: var(--page-bg);
  }
  .card {
    position: absolute;
    left: 170px;
    top: 261px;
    width: 860px;
    height: 478px;
    background: var(--card-red);
    overflow: hidden;
  }
  .brand-dot {
    position: absolute;
    left: 119px;
    top: 171px;
    width: 96px;
    height: 96px;
    border-radius: 50%;
    background: var(--accent-yellow);
  }
  .brand-name {
    position: absolute;
    left: 40px;
    top: 330px;
    width: 254px;
    margin: 0;
    text-align: center;
    font-family: "Open Sans", sans-serif;
    font-weight: 700;
    font-size: 26px;
    line-height: 34px;
    color: var(--text-white);
  }
  .offer {
    position: absolute;
    right: 69px;
    top: 104px;
    margin: 0;
    font-family: "Montserrat", sans-serif;
    font-weight: 800;
    font-size: 44px;
    line-height: 1;
    color: var(--accent-yellow);
  }
  .benefits {
    position: absolute;
    right: 32px;
    top: 184px;
    margin: 0;
    padding: 0;
    list-style: none;
  }
  .benefit {
    display: flex;
    align-items: center;
    justify-content: flex-end;
    gap: 19px;
    margin-bottom: 25px;
    font-family: "Montserrat", sans-serif;
    font-weight: 700;
    font-size: 20.5px;
    line-height: 24px;
    color: var(--text-white);
    text-align: right;
  }
  .benefit-arrow {
    flex: none;
    width: 19px;
    height: 24px;
  }
  .copyright {
    position: absolute;
    left: 0;
    right: 0;
    top: 435px;
    margin: 0;
    text-align: center;
    font-family: "Montserrat", sans-serif;
    font-weight: 600;
    font-size: 14px;
    color: var(--text-white);
  }
</style>
</head>
<body>
  <section class="card">
    <span class="brand-dot"></span>
    <p class="brand-name">Quillora.net</p>

    <h2 class="offer">FREE</h2>

    <ul class="benefits">
      <li class="benefit">
        <span>Cut study time down by up to 50%</span>
        <svg class="benefit-arrow" viewBox="0 0 19 24"><path d="M2 12 L17 3 L17 21 Z" fill="var(--accent-yellow)" stroke="var(--accent-yellow)" stroke-width="3" stroke-linejoin="round"/></svg>
      </li>
      <li class="benefit">
        <span>Learn a subject without having<br>to go to class</span>
        <svg class="benefit-arrow" viewBox="0 0 19 24"><path d="M2 12 L17 3 L17 21 Z" fill="var(--accent-yellow)" stroke="var(--accent-yellow)" stroke-width="3" stroke-linejoin="round"/></svg>
      </li>
      <li class="benefit">
        <span>Memorize anything quickly</span>
        <svg class="benefit-arrow" viewBox="0 0 19 24"><path d="M2 12 L17 3 L17 21 Z" fill="var(--accent-yellow)" stroke="var(--accent-yellow)" stroke-width="3" stroke-linejoin="round"/></svg>
      </li>
    </ul>

    <p class="copyright">Copyright Brightpath Services, LLC 2013-2022 All Rights Reserved</p>
  </section>
</body>
</html>
```